BRIARFELL Real Estate
Real Estate Developer
Project: BRIARFELL Real Estate
BRIARFELL Real Estate - Real Estate
Creative Brief
Use specific fonts
Up to the designer!
Professional
Matthias L. Halvik
Managing Director
BRIARFELL Real Estate GmbH & Co. KG Lindauer Gang 14 20417 Hamburg Germany
mlh@briarfellre.com
briarfellre.com
One-sided or two-sided cards are welcome and any of the three logos and its colour variations can be chosen!

```html
<!DOCTYPE html>
<html lang="en">
<head>
<meta charset="utf-8">
<title>BRIARFELL Real Estate – Business Card</title>
<link href="https://fonts.googleapis.com/css2?family=Montserrat:wght@500;700;800&family=Open+Sans:wght@400;600&display=swap" rel="stylesheet">
<style>
  :root {
    --bg: #d9dadb;
    --green-dark: #1f3d26;
    --green: #2f5a37;
    --green-light: #3d6b45;
    --grey: #8c8f91;
    --grey-dark: #5b5e60;
    --ink: #3a3c3d;
    --white: #ffffff;
  }
  * { margin: 0; padding: 0; box-sizing: border-box; }
  html, body { width: 1200px; height: 984px; overflow: hidden; }
  body {
    background: var(--bg);
    font-family: "Open Sans", Arial, sans-serif;
    position: relative;
  }
  .card {
    position: absolute;
    width: 620px;
    height: 400px;
    border-radius: 22px;
    overflow: hidden;
    box-shadow: 0 14px 30px rgba(0,0,0,0.22);
  }
  /* Back side */
  .card-back {
    left: 90px; top: 70px;
    background: radial-gradient(ellipse at 45% 40%, var(--green-light), var(--green) 45%, var(--green-dark));
    color: var(--white);
  }
  .back-brand {
    position: absolute;
    left: 0; right: 0; top: 128px;
    display: flex; align-items: center; justify-content: center; gap: 14px;
    font-family: "Montserrat", sans-serif;
    font-weight: 700;
    font-size: 40px;
    letter-spacing: 2px;
  }
  .brand-dot {
    width: 34px; height: 34px; border-radius: 50%;
    background: var(--white);
  }
  .back-url {
    position: absolute;
    left: 0; right: 0; top: 250px;
    text-align: center;
    font-family: "Montserrat", sans-serif;
    font-weight: 500;
    font-size: 26px;
    letter-spacing: 4px;
  }
  /* Front side */
  .card-front {
    left: 490px; top: 514px;
    background: var(--white);
    color: var(--ink);
  }
  .front-waves { position: absolute; left: 0; top: 0; width: 620px; height: 400px; }
  .front-brand {
    position: absolute;
    left: 230px; top: 62px;
    display: flex; align-items: center; gap: 8px;
    font-family: "Montserrat", sans-serif;
    font-weight: 800;
    font-size: 28px;
    color: var(--green);
    letter-spacing: 1px;
  }
  .front-brand .brand-dot { width: 22px; height: 22px; background: var(--green); }
  .person {
    position: absolute; left: 312px; top: 116px;
  }
  .person-name { font-size: 15px; font-weight: 600; color: var(--ink); }
  .person-role { font-size: 12px; color: var(--grey-dark); }
  .company-address {
    position: absolute;
    right: 320px; top: 156px;
    text-align: right;
    font-size: 10.5px;
    line-height: 15px;
    color: var(--grey-dark);
  }
  .contact-list {
    position: absolute;
    left: 312px; top: 156px;
    list-style: none;
    font-size: 10.5px;
    line-height: 15px;
    color: var(--grey-dark);
  }
  .contact-list li { display: flex; align-items: center; gap: 6px; }
  .contact-icon { width: 10px; height: 10px; fill: var(--grey-dark); flex: none; }
</style>
</head>
<body>

<section class="card card-back" aria-label="Card back">
  <div class="back-brand"><span class="brand-dot"></span>BRIARFELL</div>
  <div class="back-url">www.briarfellre.com</div>
</section>

<section class="card card-front" aria-label="Card front">
  <svg class="front-waves" viewBox="0 0 620 400" aria-hidden="true">
    <path d="M0 222 C170 300 420 318 620 210 L620 400 L0 400 Z" fill="#c7c9ca"/>
    <path d="M0 232 C170 310 420 326 620 222 L620 400 L0 400 Z" fill="#8c8f91"/>
    <path d="M0 248 C170 322 420 336 620 242 L620 400 L0 400 Z" fill="#ffffff"/>
    <path d="M0 262 C150 330 380 350 620 300 L620 400 L0 400 Z" fill="#2f5a37"/>
    <path d="M0 300 C160 360 380 380 620 350 L620 400 L0 400 Z" fill="#1f3d26" opacity="0.55"/>
  </svg>

  <div class="front-brand"><span class="brand-dot"></span>BRIARFELL</div>

  <div class="person">
    <div class="person-name">Matthias L. Halvik</div>
    <div class="person-role">Managing Director</div>
  </div>

  <address class="company-address" style="font-style:normal">
    BRIARFELL Real Estate<br>
    GmbH &amp; Co. KG<br>
    Lindauer Gang 14<br>
    20417 Hamburg<br>
    Germany
  </address>

  <ul class="contact-list">
    <li><svg class="contact-icon" viewBox="0 0 10 10"><path d="M2 0.5 L3.6 2.8 L2.8 3.8 C3.4 5 4.9 6.6 6.2 7.2 L7.2 6.4 L9.5 8 L8.6 9.5 C5 9.2 0.8 5 0.5 1.4 Z"/></svg>+49 40 318522</li>
    <li><svg class="contact-icon" viewBox="0 0 10 10"><rect x="2.5" y="0.5" width="5" height="9" rx="1"/></svg>+49 171 604219</li>
    <li><svg class="contact-icon" viewBox="0 0 10 10"><rect x="1" y="3" width="8" height="5"/><rect x="2.5" y="1" width="5" height="2"/></svg>+49 40 318523</li>
    <li><svg class="contact-icon" viewBox="0 0 10 10"><path d="M0.5 2 H9.5 V8 H0.5 Z M0.5 2 L5 5.5 L9.5 2" fill="none" stroke="#5b5e60" stroke-width="1"/></svg>mlh@briarfellre.com</li>
    <li><svg class="contact-icon" viewBox="0 0 10 10"><circle cx="5" cy="5" r="4.2" fill="none" stroke="#5b5e60" stroke-width="1"/><path d="M0.8 5 H9.2 M5 0.8 C3 3 3 7 5 9.2 M5 0.8 C7 3 7 7 5 9.2" fill="none" stroke="#5b5e60" stroke-width="0.8"/></svg>www.briarfellre.com</li>
  </ul>
</section>

</body>
</html>
```